IT Company requires new Business Card design.

Over the years we have had a few different business card designs. We are now due for new cards across the board for all staff. We felt this would be a good time to start fresh with a new design. Our traditional card simply had our details on the front, and a list of services on the back. We don't particularly need the list of services, we have had cards where the only thing on the rear of the card was our logo.
Feel free to be creative, we would like our tag line "Complete IT Management" to appear at some point, doesn't necessarily have to be with the logo.
I have attached samples and drafts of various previous cards we have used over the years.
Industry/Entity Type
Business
Look and feel
Each slider illustrates characteristics of the customer's brand and the style your logo design should communicate.

```html
<!DOCTYPE html>
<html lang="en">
<head>
<meta charset="utf-8">
<title>Harbour Systems – Business Card</title>
<link rel="stylesheet" href="https://fonts.googleapis.com/css2?family=Open+Sans:wght@400;600;700;800&display=swap">
<style>
  :root {
    --slate: #5e7181;
    --slate-dark: #4f6170;
    --ink: #3a3f44;
    --paper: #ffffff;
    --backdrop: #e9e6e1;
    --edge: #d8d8d8;
  }
  * { box-sizing: border-box; margin: 0; padding: 0; }
  html, body {
    width: 1200px; height: 720px; overflow: hidden;
    background: var(--backdrop);
    font-family: "Open Sans", Arial, sans-serif;
  }
  .canvas {
    position: relative; width: 1200px; height: 720px;
    display: flex; align-items: center; justify-content: center; gap: 50px;
  }
  .card {
    position: relative; width: 530px; height: 303px;
    background: var(--paper);
    box-shadow: 0 1px 0 var(--edge), 0 10px 24px rgba(0,0,0,.12);
    overflow: hidden;
  }

  /* Front */
  .front { display: flex; flex-direction: column; }
  .front__header {
    height: 40px; background: var(--slate);
    color: var(--paper); font-size: 14px;
    display: flex; align-items: center; justify-content: center;
    border-bottom: 6px solid var(--paper);
    box-shadow: 0 1px 0 var(--slate);
  }
  .front__header strong { font-weight: 700; margin-right: 4px; }
  .front__body {
    flex: 1; display: flex; flex-direction: column; align-items: center;
    justify-content: center; gap: 14px; padding-top: 6px;
  }
  .brand {
    display: flex; align-items: center; gap: 12px;
  }
  .brand__square { width: 30px; height: 30px; background: var(--slate); }
  .brand__name {
    font-weight: 800; color: var(--slate); font-size: 30px;
    letter-spacing: .5px; text-transform: uppercase; line-height: 1;
  }
  .contacts {
    display: flex; flex-direction: column; align-items: center; gap: 5px;
    color: var(--ink); font-size: 12.5px;
  }
  .contacts__row { display: flex; gap: 14px; align-items: center; }
  .contact { display: inline-flex; align-items: center; gap: 5px; white-space: nowrap; }
  .contact svg { width: 12px; height: 12px; fill: var(--ink); flex: none; }
  .front__footer {
    height: 44px; background: var(--slate);
    border-top: 6px solid var(--paper);
    box-shadow: 0 -1px 0 var(--slate);
    color: var(--paper); font-size: 14px; letter-spacing: 3px;
    text-transform: uppercase; font-weight: 600;
    display: flex; align-items: center; justify-content: center;
  }

  /* Back */
  .back { display: flex; flex-direction: column; align-items: center; justify-content: center; }
  .back__brand {
    font-weight: 800; color: var(--slate); font-size: 46px;
    text-transform: uppercase; letter-spacing: 1px; line-height: 1;
    margin-top: -20px;
  }
  .back__web {
    position: absolute; right: 34px; bottom: 26px;
    color: var(--ink); font-size: 17px; letter-spacing: 1.5px;
  }
</style>
</head>
<body>
<main class="canvas">

  <section class="card front" aria-label="Business card front">
    <header class="front__header"><strong>Daniel Moore,</strong> Operation Manager</header>
    <div class="front__body">
      <div class="brand">
        <span class="brand__square" aria-hidden="true"></span>
        <span class="brand__name">Harbour Systems</span>
      </div>
      <div class="contacts">
        <div class="contacts__row">
          <span class="contact">
            <svg viewBox="0 0 12 12" aria-hidden="true"><circle cx="6" cy="6" r="6"/><path d="M4 3h1.3l.6 1.6-.8.6a4 4 0 0 0 1.7 1.7l.6-.8 1.6.6V8a1 1 0 0 1-1 1A5 5 0 0 1 3 4a1 1 0 0 1 1-1z" fill="#fff"/></svg>
            08 5550 1842
          </span>
          <span class="contact">
            <svg viewBox="0 0 12 12" aria-hidden="true"><rect x="3" y="0.5" width="6" height="11" rx="1.2"/><rect x="4" y="2" width="4" height="6" fill="#fff"/></svg>
            0400 555 718
          </span>
          <span class="contact">
            <svg viewBox="0 0 12 12" aria-hidden="true"><rect x="3" y="1" width="6" height="4"/><rect x="1" y="5" width="10" height="6" rx="1"/><rect x="3" y="7" width="6" height="1.5" fill="#fff"/></svg>
            08 5550 1842
          </span>
        </div>
        <div class="contacts__row">
          <span class="contact">
            <svg viewBox="0 0 12 12" aria-hidden="true"><rect x="0.5" y="2" width="11" height="8" rx="1"/><path d="M1 2.5 6 7l5-4.5" stroke="#fff" stroke-width="1" fill="none"/></svg>
            daniel@harboursystems.com.au
          </span>
          <span class="contact">
            <svg viewBox="0 0 12 12" aria-hidden="true"><circle cx="6" cy="6" r="6"/><path d="M1 6h10M6 1v10M6 1c-3 3-3 7 0 10M6 1c3 3 3 7 0 10" stroke="#fff" stroke-width=".8" fill="none"/></svg>
            www.harboursystems.com.au
          </span>
        </div>
        <div class="contacts__row">
          <span class="contact">Unit 4 22 Harbour Road, Westfield WA 6000</span>
        </div>
      </div>
    </div>
    <footer class="front__footer">Complete IT Management</footer>
  </section>

  <section class="card back" aria-label="Business card back">
    <div class="back__brand">Harbour Systems</div>
    <div class="back__web">www.harboursystems.com.au</div>
  </section>

</main>
</body>
</html>
```